FOOD SUPPLEMENT FOR SOAR THROAT - TOLVERANE

I need a design for a food supplement product. The product is a formulation designed to combat bacteria that causes infections in the throat. Due to the fact that is a food supplment the design has to be away from the regular farmacy products. The design has to be elegant in the same time to shows the seriousness of the product. Need to have 3 pictograms for gluten , sugar and lactose free, the photo of the ingredients is an option. As colors yellow, orange, lime green and dark blue is preferable. In attached the dimensions of the box, the logo of the name of the product and the old box where the 3 pictograms Ithe ingredients are Murraya paniculata, Vitamin C, Malva sylvestris and Filipendula ulmaria. The title under the name is Food supplement in functional chewing gum and in italian Integratore alimentare in chewing gum funzionale.

pharmaceutical

Colors
0054AA
0677BA
7BADD7
CADEEF
E8F1F8
59FF00
82FF00
B8FF75
E3FFCB
F4FFEA
FFF300
FFF600
FEFA6F
FFFEC7
FFFEE8
F0912C
F2A743
F7CA91
FBE8D2
FDF5EE

Must have
• pictograms -gluten, lactose, sugar free

```html
<!DOCTYPE html>
<html lang="en">
<head>
<meta charset="utf-8">
<title>TOLVERANE – Food supplement in Chewing Gum</title>
<link rel="stylesheet" href="https://fonts.googleapis.com/css2?family=Fira+Sans:ital,wght@0,500;0,600;0,800;1,400;1,500&display=swap">
<style>
  :root{
    --stage:#07955A;
    --panel:#FFFFFF;
    --lime-deep:#7CC52A;
    --lime:#B8FF75;
    --lime-pale:#F4FFEA;
    --name:#DCEB1A;
    --ink:#333A3F;
    --badge-blue:#2E6FA8;
    --label-teal:#17917C;
    --band-grey-top:#C9CBCD;
    --band-grey-bot:#8E9296;
    --band-blue:#2F74A8;
    --band-teal:#1E8C78;
    --seal-green:#129A4B;
  }
  *{margin:0;padding:0;box-sizing:border-box}
  html,body{width:1200px;height:875px;overflow:hidden}
  body{background:var(--stage);font-family:"Fira Sans",sans-serif;position:relative}
  .box-front{
    position:absolute;left:80px;top:138px;width:1040px;height:600px;
    background:var(--panel);overflow:hidden;
  }
  .swoosh{position:absolute;inset:0}
  .brand{
    position:absolute;left:190px;top:118px;display:flex;align-items:center;gap:18px;
  }
  .brand-dot{width:34px;height:34px;border-radius:50%;background:var(--lime-deep)}
  .brand-name{
    font-weight:800;font-size:90px;letter-spacing:1px;color:var(--name);line-height:1;
  }
  .subtitle{
    position:absolute;left:318px;top:226px;font-style:italic;font-weight:500;
    font-size:27px;line-height:34px;color:var(--ink);text-align:center;
  }
  .pictograms{position:absolute;left:105px;top:318px;display:flex;gap:28px}
  .picto{display:flex;flex-direction:column;align-items:center;width:118px}
  .picto svg{width:108px;height:78px;display:block}
  .picto-label{
    margin-top:6px;font-style:italic;font-weight:500;font-size:20px;line-height:24px;
    color:var(--label-teal);white-space:nowrap;
  }
  .seal{position:absolute;right:38px;top:258px;width:150px;height:150px}
  .ingredient-band{
    position:absolute;left:0;top:444px;width:100%;height:48px;
    background:linear-gradient(180deg,var(--band-grey-top),var(--band-grey-bot));
    display:flex;align-items:center;padding-left:92px;
  }
  .ingredients{
    color:#fff;font-weight:600;font-size:23px;letter-spacing:.4px;
    text-shadow:0 1px 2px rgba(0,0,0,.35);
  }
  .italian-band{
    position:absolute;left:0;top:492px;width:100%;height:108px;
    background:linear-gradient(90deg,var(--band-blue) 0%,var(--band-teal) 55%,var(--band-teal) 100%);
    padding:18px 0 0 92px;
  }
  .italian{color:#fff;font-style:italic;font-weight:400;font-size:29px;line-height:35px}
</style>
</head>
<body>
  <section class="box-front">
    <svg class="swoosh" viewBox="0 0 1040 600" preserveAspectRatio="none" aria-hidden="true">
      <defs>
        <linearGradient id="sweep" x1="0" y1="0" x2="1" y2="0">
          <stop offset="0" stop-color="#F4FFEA"/>
          <stop offset=".45" stop-color="#B8FF75"/>
          <stop offset="1" stop-color="#6CC02C"/>
        </linearGradient>
        <linearGradient id="glow" x1="0" y1="0" x2="1" y2="0">
          <stop offset="0" stop-color="#FFFFFF" stop-opacity="0"/>
          <stop offset=".6" stop-color="#FFFFFF" stop-opacity=".85"/>
          <stop offset="1" stop-color="#FFFFFF" stop-opacity=".2"/>
        </linearGradient>
      </defs>
      <path d="M740 0 C860 90 860 300 560 444 L1040 444 L1040 0 Z" fill="url(#sweep)"/>
      <path d="M900 0 C1010 120 960 300 820 444 L1040 444 L1040 0 Z" fill="url(#glow)"/>
      <path d="M980 0 C1040 140 1010 320 940 444 L1040 444 L1040 0 Z" fill="#F4FFEA" opacity=".6"/>
    </svg>

    <div class="brand">
      <span class="brand-dot"></span>
      <h1 class="brand-name">TOLVERANE</h1>
    </div>

    <p class="subtitle">Food supplement in<br>Chewing Gum</p>

    <div class="pictograms">
      <div class="picto">
        <svg viewBox="0 0 108 78" aria-hidden="true">
          <path d="M6 10 H102 V44 A34 34 0 0 1 68 78 H40 A34 34 0 0 1 6 44 Z" fill="var(--badge-blue)"/>
          <circle cx="54" cy="40" r="22" fill="none" stroke="#fff" stroke-width="4"/>
          <rect x="43" y="31" width="10" height="10" fill="#fff"/>
          <rect x="55" y="37" width="10" height="10" fill="#fff"/>
          <line x1="38" y1="56" x2="70" y2="24" stroke="#fff" stroke-width="4"/>
        </svg>
        <span class="picto-label">Sugar Free</span>
      </div>
      <div class="picto">
        <svg viewBox="0 0 108 78" aria-hidden="true">
          <path d="M6 10 H102 V44 A34 34 0 0 1 68 78 H40 A34 34 0 0 1 6 44 Z" fill="var(--badge-blue)"/>
          <circle cx="54" cy="40" r="22" fill="none" stroke="#fff" stroke-width="4"/>
          <line x1="54" y1="24" x2="54" y2="58" stroke="#fff" stroke-width="3"/>
          <ellipse cx="48" cy="32" rx="4" ry="6" fill="#fff"/>
          <ellipse cx="60" cy="32" rx="4" ry="6" fill="#fff"/>
          <ellipse cx="48" cy="44" rx="4" ry="6" fill="#fff"/>
          <ellipse cx="60" cy="44" rx="4" ry="6" fill="#fff"/>
          <line x1="38" y1="56" x2="70" y2="24" stroke="#fff" stroke-width="4"/>
        </svg>
        <span class="picto-label">GlutenFree</span>
      </div>
      <div class="picto">
        <svg viewBox="0 0 108 78" aria-hidden="true">
          <path d="M6 10 H102 V44 A34 34 0 0 1 68 78 H40 A34 34 0 0 1 6 44 Z" fill="var(--badge-blue)"/>
          <circle cx="54" cy="40" r="22" fill="none" stroke="#fff" stroke-width="4"/>
          <path d="M50 24 H58 V30 L62 36 V56 H46 V36 L50 30 Z" fill="#fff"/>
          <line x1="38" y1="56" x2="70" y2="24" stroke="var(--badge-blue)" stroke-width="7"/>
          <line x1="38" y1="56" x2="70" y2="24" stroke="#fff" stroke-width="4"/>
        </svg>
        <span class="picto-label">Lactose Free</span>
      </div>
    </div>

    <svg class="seal" viewBox="0 0 150 150" role="img" aria-label="30 chewing gums">
      <defs>
        <path id="arc-top" d="M28 75 A47 47 0 0 1 122 75"/>
        <path id="arc-bottom" d="M30 82 A45 45 0 0 0 120 82"/>
        <radialGradient id="silver" cx=".5" cy=".4" r=".6">
          <stop offset="0" stop-color="#FFFFFF"/>
          <stop offset="1" stop-color="#B9BDC1"/>
        </radialGradient>
      </defs>
      <circle cx="75" cy="75" r="72" fill="#2E6FA8"/>
      <circle cx="75" cy="75" r="66" fill="url(#silver)"/>
      <circle cx="75" cy="75" r="38" fill="#E4E6E8" stroke="#FFFFFF" stroke-width="3"/>
      <text font-family="Fira Sans, sans-serif" font-weight="800" font-size="17" fill="#FFFFFF" stroke="#2E6FA8" stroke-width=".8" letter-spacing="1">
        <textPath href="#arc-top" startOffset="50%" text-anchor="middle">CHEWING</textPath>
      </text>
      <text font-family="Fira Sans, sans-serif" font-weight="800" font-size="16" fill="#FFFFFF" stroke="#7A8085" stroke-width=".8" letter-spacing="1" dy="14">
        <textPath href="#arc-bottom" startOffset="50%" text-anchor="middle">GUMS</textPath>
      </text>
      <text x="75" y="92" text-anchor="middle" font-family="Fira Sans, sans-serif" font-weight="800" font-size="46" fill="var(--seal-green)">30</text>
    </svg>

    <div class="ingredient-band">
      <p class="ingredients">Murraya paniculata, Vitamin C, Malva sylvestris and Filipendula ulmaria</p>
    </div>

    <div class="italian-band">
      <p class="italian">Integratore alimentare in<br>Chewing Gum</p>
    </div>
  </section>
</body>
</html>
```